Small Business Consulting Firm Needs Business Card Design

Need a sleek modern business card with 2 sides matching the colors of our logo. We will be placing these with a mailer we are sending out. These business cards will only ever be given to business owners. We operate helping businesses who are struggling with cash flow or finances. If the green and blue design needs to be moved to the right of "Harborline Crest Consulting" for aesthetic purposes that is ok. We will need an editable file if possible. We would like to include the reps name, email, website, and phone number. For now just use Peter Vance, pvance@harborlinecrest.com, www.harborlinecrest.com, and 833-555-0172.

```html
<!DOCTYPE html>
<html lang="en">
<head>
<meta charset="utf-8">
<title>Harborline Crest Consulting – Business Card</title>
<link href="https://fonts.googleapis.com/css2?family=Roboto:wght@500&family=Lato:wght@400&family=Open+Sans:wght@400&display=swap" rel="stylesheet">
<style>
  :root {
    --brand-blue: #0080c8;
    --brand-green: #63a23a;
    --ink: #3d3d3d;
    --muted: #666666;
    --paper: #ffffff;
    --backdrop: #c9c9c9;
  }
  * { box-sizing: border-box; margin: 0; padding: 0; }
  html, body {
    width: 1125px; height: 1200px; overflow: hidden;
    background: var(--backdrop);
  }
  .canvas { position: relative; width: 1125px; height: 1200px; }

  .card {
    position: absolute; left: 178px; width: 768px; height: 436px;
    border-radius: 24px; overflow: hidden;
  }
  .card--front { top: 140px; background: var(--paper); }
  .card--back  { top: 626px; background: var(--brand-blue); }

  .accent-tab {
    position: absolute; left: 0; top: 187px; width: 33px; height: 62px;
    background: var(--brand-green);
  }

  .brand {
    position: absolute; left: 42px; width: 320px; top: 118px;
    display: flex; flex-direction: column; align-items: center;
    font-family: "Open Sans", sans-serif; font-weight: 400;
    color: var(--ink); text-align: center;
  }
  .brand__square { width: 62px; height: 62px; background: var(--brand-green); margin-bottom: 26px; }
  .brand__name { font-size: 23px; letter-spacing: 1.5px; line-height: 1.1; }
  .brand__sub { font-size: 13px; letter-spacing: 8px; margin-top: 8px; padding-left: 8px; }

  .divider { position: absolute; left: 384px; width: 2px; background: var(--brand-green); }
  .divider--name { top: 98px; height: 59px; }
  .divider--contact { top: 272px; height: 88px; }

  .rep { position: absolute; left: 403px; top: 90px; font-family: "Roboto", sans-serif; font-weight: 500; }
  .rep__name { font-size: 33px; color: var(--brand-green); letter-spacing: 1px; line-height: 1.2; }
  .rep__title { font-size: 21px; color: var(--brand-blue); margin-top: 2px; }

  .address-band {
    position: absolute; left: 384px; top: 187px; width: 384px; height: 62px;
    background: var(--brand-blue); color: var(--paper);
    font-family: "Lato", sans-serif; font-size: 17.5px; line-height: 22px;
    padding: 9px 0 0 19px;
  }

  .contact-list {
    position: absolute; left: 403px; top: 269px; list-style: none;
    font-family: "Lato", sans-serif; font-size: 18.5px; color: var(--muted);
  }
  .contact-list li { display: flex; align-items: center; height: 24px; }
  .contact-list svg { width: 14px; height: 14px; margin-right: 9px; fill: var(--brand-green); flex: none; }

  .brand--reverse { left: 184px; width: 400px; top: 112px; color: var(--paper); }
  .brand--reverse .brand__square { width: 100px; height: 100px; background: var(--paper); margin-bottom: 36px; }
  .brand--reverse .brand__name { font-size: 32px; letter-spacing: 2px; }
  .brand--reverse .brand__sub { font-size: 18px; letter-spacing: 12px; padding-left: 12px; margin-top: 10px; }
</style>
</head>
<body>
<div class="canvas">

  <section class="card card--front">
    <div class="accent-tab"></div>

    <div class="brand">
      <div class="brand__square"></div>
      <div class="brand__name">HARBORLINE CREST</div>
      <div class="brand__sub">CONSULTING</div>
    </div>

    <div class="divider divider--name"></div>
    <div class="rep">
      <div class="rep__name">Peter Vance</div>
      <div class="rep__title">General Manager</div>
    </div>

    <div class="address-band">
      1480 W Brookfield Ave Dalton,<br>Marren County 70412 USA
    </div>

    <div class="divider divider--contact"></div>
    <ul class="contact-list">
      <li>
        <svg viewBox="0 0 16 16"><path d="M3.5 1 6 3.8 4.7 5.6c.8 2 2.6 3.9 4.7 4.7L11.2 9 14 11.5 12.5 14C6.8 14 2 9.2 2 3.5z"/></svg>
        833-555-0172
      </li>
      <li>
        <svg viewBox="0 0 16 16"><path d="M4 1h8v14H4zM5.5 2.5v9h5v-9zM7 12.5h2v1H7z" fill-rule="evenodd"/></svg>
        0455 000 321
      </li>
      <li>
        <svg viewBox="0 0 16 16"><path d="M1 3h14v10H1zM2.5 5v6.5h11V5L8 9z" fill-rule="evenodd"/></svg>
        pvance@harborlinecrest.com
      </li>
      <li>
        <svg viewBox="0 0 16 16"><path d="M8 1a7 7 0 1 0 0 14A7 7 0 0 0 8 1zm0 1.6a5.4 5.4 0 1 1 0 10.8A5.4 5.4 0 0 1 8 2.6zM5 4.5l2 1.5-1 2 1.5 1.5-.5 2.5-2-2-1-3zm5 0 1.5 2-1 2.5-1.5-1 .5-2z"/></svg>
        www.harborlinecrest.com
      </li>
    </ul>
  </section>

  <section class="card card--back">
    <div class="brand brand--reverse">
      <div class="brand__square"></div>
      <div class="brand__name">HARBORLINE CREST</div>
      <div class="brand__sub">CONSULTING</div>
    </div>
  </section>

</div>
</body>
</html>
```